TR Stationery - Modern Contemporary

Develop modern template for Letterhead and Stationery (business card, letterhead, envelopes) using the TR Logo and Icon

Colors
0054AA
0677BA
7BADD7
CADEEF
E8F1F8
00AB8E
00BBA5
67D7C9
C6EFE9
E9F9F6
EE7325
F08F49
F5BC92
FAE3D3
FDF4ED
6B429C
8869AF
B7A5CE
E3DAEB
F3F0F8

```html
<!DOCTYPE html>
<html lang="en">
<head>
<meta charset="utf-8">
<title>TR Stationery – Business Card</title>
<link href="https://fonts.googleapis.com/css2?family=Poppins:wght@300;400;500&family=Montserrat:wght@700&display=swap" rel="stylesheet">
<style>
  :root{
    --backdrop:#d6d0c8;
    --card-light:#efedea;
    --card-mid:#e2dfdb;
    --panel-dark:#262835;
    --panel-dark-2:#363848;
    --brand-green:#1a9a4a;
    --ink:#15161c;
    --panel-text:#e6e6ec;
  }
  html,body{margin:0;padding:0;width:1200px;height:969px;overflow:hidden;background:var(--backdrop);}
  .card{
    position:absolute;left:166px;top:226px;width:868px;height:495px;
    border-radius:22px;overflow:hidden;
    background:linear-gradient(160deg,var(--card-light),var(--card-mid));
    box-shadow:0 18px 40px rgba(0,0,0,.18);
    font-family:"Poppins",sans-serif;
  }
  .card-decoration{
    position:absolute;left:0;top:0;width:455px;height:100%;
    background:linear-gradient(172deg,
      rgba(26,154,74,.55) 0%,
      rgba(54,56,72,.9) 30%,
      var(--panel-dark) 60%,
      var(--panel-dark-2) 100%);
  }
  .brand-name{
    position:absolute;right:73px;top:94px;margin:0;
    font-weight:500;font-size:48px;letter-spacing:.5px;
    color:var(--ink);line-height:1;
  }
  .holder{position:absolute;right:72px;top:326px;text-align:right;}
  .holder-name{margin:0;font-family:"Montserrat",sans-serif;font-weight:700;font-size:29px;color:var(--ink);letter-spacing:.3px;line-height:1.1;}
  .holder-role{margin:3px 0 0;font-size:20px;font-weight:400;color:var(--brand-green);line-height:1.1;}
  .contact-list{position:absolute;left:66px;top:290px;margin:0;padding:0;list-style:none;color:var(--panel-text);font-size:19px;font-weight:300;line-height:24px;}
  .contact-list li{display:flex;align-items:flex-start;gap:10px;margin-bottom:1px;}
  .contact-list svg{flex:0 0 16px;width:16px;height:16px;margin-top:4px;fill:var(--brand-green);}
</style>
</head>
<body>
  <section class="card" aria-label="TR Stationery business card">
    <div class="card-decoration" role="img" aria-label="Decorative side panel in charcoal with green and orange accents"></div>

    <h1 class="brand-name">TR Stationery</h1>

    <div class="holder">
      <p class="holder-name">DANIEL REYES</p>
      <p class="holder-role">President</p>
    </div>

    <ul class="contact-list">
      <li><svg viewBox="0 0 16 16"><path d="M8 0a5.5 5.5 0 0 0-5.5 5.5C2.5 10 8 16 8 16s5.5-6 5.5-10.5A5.5 5.5 0 0 0 8 0zm0 8a2.5 2.5 0 1 1 0-5 2.5 2.5 0 0 1 0 5z"/></svg><span>1420 Willow Court<br>Juneau, Alaska 99801</span></li>
      <li><svg viewBox="0 0 16 16"><path d="M3.6 1l2.3 3-1.4 1.7c.9 2 2.6 3.7 4.6 4.6l1.7-1.4 3 2.3-1.3 2.6C7 13.5 2.5 9 1 3.6z"/></svg><span>555-214-0386</span></li>
      <li><svg viewBox="0 0 16 16"><path d="M4.5 0h7a1 1 0 0 1 1 1v14a1 1 0 0 1-1 1h-7a1 1 0 0 1-1-1V1a1 1 0 0 1 1-1zm.5 2v11h6V2zm3 11.6a.8.8 0 1 0 0 1.6.8.8 0 0 0 0-1.6z"/></svg><span>555-608-7123</span></li>
      <li><svg viewBox="0 0 16 16"><path d="M1 3h14v10H1zm1.2 1.2L8 8.6l5.8-4.4z"/></svg><span>hello@trstationery.com</span></li>
      <li><svg viewBox="0 0 16 16"><path d="M8 0a8 8 0 1 0 0 16A8 8 0 0 0 8 0zm-1 14.4A6.5 6.5 0 0 1 2.6 5.5L6 9v1l1 1zm5.3-2.5c-.2-.6-.8-1-1.4-1H10V9l-1-1H5V6h2V4h1.5l.5-2a6.5 6.5 0 0 1 3.3 9.9z"/></svg><span>trstationery.com</span></li>
    </ul>
  </section>
</body>
</html>
```